Dean harlow realestate

We want something complete different to our website now and something that will stand out this is our website http://deanharlowrealestate-example.com/

our company website for my boss is www.trevorvance-example.com

please note this website is being made for dean harlow not trevor vance

something similar to our company website but has to be in the branding of dean harlow realestate

```html
<!DOCTYPE html>
<html lang="en">
<head>
<meta charset="utf-8">
<title>Dean Harlow Property</title>
<link rel="stylesheet" href="https://fonts.googleapis.com/css2?family=Cinzel:wght@400;700&family=Montserrat:wght@400;600;700&family=Open+Sans:wght@400;600;700&display=swap">
<style>
:root{
  --blue:#2196f3;
  --blue-dark:#1a7fd4;
  --green:#2ecc71;
  --ink:#222a33;
  --text:#666;
  --muted:#999;
  --line:#e3e3e3;
  --panel:#f5f5f5;
  --dark:#2f2f2f;
  --darker:#232323;
  --white:#fff;
}
*{box-sizing:border-box;margin:0;padding:0}
html,body{width:1200px;height:4942px;overflow:hidden}
body{position:relative;background:var(--white);font-family:"Open Sans",Arial,sans-serif;color:var(--text);font-size:13px}
.section{position:absolute;left:0;width:1200px}
.section-title{position:absolute;left:0;width:1200px;text-align:center;font-family:"Cinzel",Georgia,serif;font-size:31px;letter-spacing:2px;color:var(--ink)}
.section-title::after{content:"";display:block;width:50px;height:3px;background:var(--ink);margin:12px auto 0}
.lead{position:absolute;left:99px;width:1002px;text-align:center;font-size:12px;line-height:20px;color:var(--text)}

.site-header{top:0;height:99px;background:var(--white)}
.brand{position:absolute;left:82px;top:16px;display:flex;align-items:center;gap:12px}
.brand-mark{width:54px;height:54px;background:var(--blue)}
.brand-name{font-family:"Cinzel",Georgia,serif;font-weight:700;font-size:22px;line-height:26px;color:var(--ink);letter-spacing:1px}
.main-nav{position:absolute;right:95px;top:48px;display:flex;gap:22px;font-family:"Montserrat",Arial,sans-serif;font-weight:600;font-size:15px;color:var(--ink)}

.hero{top:99px;height:561px}
.hero-photo{position:absolute;inset:0;background:linear-gradient(100deg,#d9dcdf 0%,#f4f5f4 35%,#c9d7cf 55%,#8a8c8a 80%,#4a4846 100%)}
.hero-bar{position:absolute;left:0;top:494px;width:1200px;height:60px;background:linear-gradient(90deg,rgba(20,20,20,.75),rgba(20,20,20,.35))}
.hero-address{position:absolute;left:99px;top:20px;color:var(--white);font-size:13px;font-family:"Montserrat",Arial,sans-serif;text-transform:uppercase}
.hero-details{position:absolute;left:725px;top:0;width:99px;height:60px;background:var(--blue);color:var(--white);font-size:14px;display:flex;align-items:center;justify-content:center;gap:6px}
.hero-price{position:absolute;left:824px;top:0;width:182px;height:60px;background:var(--green);color:var(--white);font-family:"Montserrat",Arial,sans-serif;font-weight:700;font-size:22px;display:flex;align-items:center;justify-content:center}
.hero-arrow{position:absolute;top:0;width:57px;height:60px;background:var(--blue);display:flex;align-items:center;justify-content:center}
.hero-arrow.prev{left:1006px;border-right:1px solid var(--blue-dark)}
.hero-arrow.next{left:1064px}

.search{top:660px;height:247px;background:var(--panel)}
.field-label{position:absolute;top:47px;font-size:14px;color:var(--ink)}
.field-select{position:absolute;top:84px;width:231px;height:36px;background:var(--white);border:1px solid #d6d6d6;font-size:12px;color:var(--muted);padding:9px 10px}
.field-select::after{content:"";position:absolute;right:10px;top:14px;border:5px solid transparent;border-top-color:#777}
.range-label{position:absolute;left:99px;top:135px;font-size:14px;color:var(--ink)}
.range-track{position:absolute;left:99px;top:172px;width:488px;height:6px;background:#cfcfcf;border-radius:3px}
.range-fill{position:absolute;left:95px;top:0;width:300px;height:6px;background:var(--blue)}
.range-knob{position:absolute;top:-7px;width:20px;height:20px;border-radius:50%;background:var(--white);border:1px solid #bbb}
.range-value{position:absolute;left:610px;top:163px;font-family:"Montserrat",Arial,sans-serif;font-weight:700;font-size:19px;color:var(--blue)}
.btn-search{position:absolute;left:864px;top:151px;width:224px;height:42px;background:var(--blue);color:var(--white);font-family:"Montserrat",Arial,sans-serif;font-weight:600;font-size:14px;display:flex;align-items:center;justify-content:center}

.about{top:907px;height:560px}
.about .section-title{top:58px}
.about .lead{top:131px}
.sub-title{position:absolute;left:99px;font-family:"Montserrat",Arial,sans-serif;font-weight:700;font-size:24px;color:var(--blue);text-transform:uppercase}
.about-text{position:absolute;left:99px;width:470px;font-size:12px;line-height:19px}
.about-video{position:absolute;left:603px;top:220px;width:485px;height:307px;background:linear-gradient(160deg,#8fa9c4 0%,#c3cbd0 45%,#6f8b8a 70%,#2e7fb2 100%)}
.play{position:absolute;left:212px;top:105px;width:60px;height:60px;border-radius:50%;border:2px solid var(--white);display:flex;align-items:center;justify-content:center}
.video-caption{position:absolute;left:165px;top:195px;color:var(--white);font-family:"Montserrat",Arial,sans-serif;font-weight:700;font-size:24px}
.video-caption small{display:block;font-size:10px;font-weight:400;letter-spacing:1px}

.featured{top:1467px;height:1263px}
.featured .section-title{top:48px}
.featured .lead{top:138px}
.tabs{position:absolute;left:224px;top:233px;display:flex;gap:10px}
.tab{height:40px;padding:0 22px;border:1px solid #bcd9f3;background:var(--white);font-family:"Montserrat",Arial,sans-serif;font-size:12px;color:var(--ink);display:flex;align-items:center;text-transform:uppercase}
.tab.active{background:var(--blue);border-color:var(--blue);color:var(--white)}
.prop-card{position:absolute;width:306px;height:248px;background:var(--white);border:1px solid var(--line)}
.prop-photo{position:absolute;left:0;top:0;width:304px;height:180px}
.tag-sale{position:absolute;right:0;top:0;width:44px;height:56px;background:var(--blue);color:var(--white);font-size:11px;font-weight:700;line-height:14px;padding:8px 0 0 8px}
.prop-name{position:absolute;left:12px;top:195px;font-family:"Montserrat",Arial,sans-serif;font-weight:700;font-size:12px;color:var(--ink)}
.prop-loc{position:absolute;left:12px;top:215px;font-size:11px;color:var(--muted)}
.prop-price{position:absolute;right:14px;top:208px;font-weight:700;font-size:12px;color:var(--blue)}
.btn-more{position:absolute;left:483px;top:1144px;width:222px;height:56px;background:var(--blue);color:var(--white);font-family:"Montserrat",Arial,sans-serif;font-weight:600;font-size:15px;display:flex;align-items:center;justify-content:center}

.highlights{top:2763px;height:468px;background:linear-gradient(90deg,#2b2b2b,#3a3a3a 50%,#2e2e2e)}
.hl-title{position:absolute;left:99px;top:52px;font-family:"Montserrat",Arial,sans-serif;font-weight:600;font-size:34px;letter-spacing:3px;color:var(--white)}
.hl-text{position:absolute;left:99px;top:110px;width:480px;font-size:12px;line-height:19px;color:#ccc}
.hl-feature{position:absolute;width:230px}
.hl-feature svg{position:absolute;left:0;top:2px}
.hl-feature h4{margin-left:34px;font-family:"Montserrat",Arial,sans-serif;font-size:13px;color:var(--white)}
.hl-feature p{margin-left:34px;font-size:11px;line-height:17px;color:#aaa;margin-top:4px}
.btn-green{position:absolute;left:99px;top:340px;width:120px;height:40px;background:var(--green);color:var(--white);font-family:"Montserrat",Arial,sans-serif;font-size:12px;font-weight:600;display:flex;align-items:center;justify-content:center}
.hl-photo{position:absolute;left:610px;top:46px;width:478px;height:372px;background:linear-gradient(170deg,#8fb9e0 0%,#d8dfe4 45%,#a4a8a6 62%,#2f9ad0 85%)}
.hl-arrow{position:absolute;top:200px;width:30px;height:40px;background:var(--green);display:flex;align-items:center;justify-content:center}

.listings{top:3231px;height:527px}
.listings .section-title{top:48px}
.list-card{position:absolute;top:158px;width:313px;height:310px;background:var(--white);border:1px solid var(--line);box-shadow:0 2px 6px rgba(0,0,0,.08)}
.list-photo{position:absolute;left:0;top:0;width:311px;height:188px}
.tag-excl{position:absolute;right:10px;top:10px;background:var(--ink);color:var(--white);font-size:9px;padding:3px 7px;text-transform:uppercase}
.tag-rent{position:absolute;left:10px;top:162px;background:rgba(0,0,0,.65);color:var(--white);font-size:10px;font-weight:700;padding:4px 8px}
.list-name{position:absolute;left:14px;top:198px;font-family:"Montserrat",Arial,sans-serif;font-weight:700;font-size:12px;color:var(--ink)}
.list-addr{position:absolute;left:14px;top:218px;font-size:9px;color:var(--muted)}
.list-spec{position:absolute;left:14px;top:234px;width:284px;font-size:10px;line-height:14px;color:var(--text)}
.list-foot{position:absolute;left:14px;right:14px;top:284px;border-top:1px solid var(--line);padding-top:6px;display:flex;justify-content:space-between;font-size:9px;color:var(--muted)}
.side-arrow{position:absolute;top:320px;width:44px;height:44px;background:var(--blue);display:flex;align-items:center;justify-content:center}

.testimonial{top:3758px;height:422px;background:linear-gradient(180deg,#1d1d1f,#2c2a28 50%,#1a1a1c)}
.testimonial .section-title{top:52px;color:var(--white)}
.testimonial .section-title::after{background:var(--white)}
.client-photo{position:absolute;left:171px;top:150px;width:232px;height:232px;border-radius:50%;background:radial-gradient(circle at 50% 40%,#d9c2ae,#8a7463 60%,#3d3733);border:4px solid #555}
.quote{position:absolute;left:445px;top:190px;width:640px;font-size:15px;line-height:27px;color:#ddd}
.client-name{position:absolute;left:445px;top:272px;font-size:14px;color:var(--blue)}
.dots{position:absolute;left:560px;top:326px;display:flex;gap:10px}
.dots span{width:40px;height:3px;background:#777}
.dots span.on{background:var(--blue)}

.newsletter{top:4180px;height:337px;background:var(--blue)}
.newsletter .section-title{top:122px;color:var(--white)}
.newsletter .section-title::after{display:none}
.news-input{position:absolute;left:204px;top:222px;width:604px;height:40px;background:var(--white);font-size:12px;color:var(--muted);padding:12px 14px}
.news-btn{position:absolute;left:808px;top:222px;width:165px;height:40px;background:#333;color:var(--white);font-family:"Montserrat",Arial,sans-serif;font-size:13px;font-weight:600;display:flex;align-items:center;justify-content:center}

.site-footer{top:4517px;height:379px;background:var(--dark)}
.foot-col{position:absolute;top:44px;width:240px}
.foot-col h5{font-family:"Montserrat",Arial,sans-serif;font-size:12px;color:var(--white);text-transform:uppercase;letter-spacing:1px;margin-bottom:18px}
.foot-col p,.foot-col li{font-size:11px;line-height:18px;color:#aaa;list-style:none}
.contact-line{display:flex;align-items:center;gap:8px;margin-top:10px}
.post{display:flex;gap:10px;margin-bottom:14px}
.post-thumb{width:46px;height:40px;flex:none;background:linear-gradient(135deg,#8a8f95,#c9c5bd)}
.post b{display:block;font-size:11px;line-height:15px;color:#ddd;font-weight:600}
.post small{font-size:9px;color:var(--blue)}
.quick li{border-bottom:1px solid #444;padding:5px 0;font-size:10px}
.tweet{margin-bottom:14px}
.tweet b{color:var(--blue);font-weight:600}
.copyright{top:4896px;height:46px;background:var(--darker)}
.copy-text{position:absolute;left:73px;top:14px;font-size:12px;color:#bbb}
.social{position:absolute;right:82px;top:15px;display:flex;gap:16px}
.social span{width:16px;height:16px;background:#bbb}
</style>
</head>
<body>

<header class="section site-header">
  <div class="brand">
    <div class="brand-mark"></div>
    <div class="brand-name">Dean Harlow<br>Property</div>
  </div>
  <nav class="main-nav">
    <span>HOME</span><span>ABOUT</span><span>FOR SALE</span><span>AGENTS</span><span>BOOK APPRAISAL</span><span>CONTACT</span>
  </nav>
</header>

<section class="section hero">
  <div class="hero-photo" role="img" aria-label="Bright modern living room with white sofa, black armchairs and a glass wall opening onto a lawn"></div>
  <div class="hero-bar">
    <div class="hero-address">18 Harbour Crest Road, Linden Bay, NSW 2040</div>
    <div class="hero-details">
      <svg width="14" height="14" viewBox="0 0 14 14"><rect x="1" y="1" width="12" height="12" fill="none" stroke="#fff" stroke-width="1.5"/><path d="M4 5h6M4 8h6" stroke="#fff" stroke-width="1.5"/></svg>
      Details
    </div>
    <div class="hero-price">$359,000.00</div>
    <div class="hero-arrow prev"><svg width="10" height="14" viewBox="0 0 10 14"><path d="M8 1L2 7l6 6" fill="none" stroke="#fff" stroke-width="2"/></svg></div>
    <div class="hero-arrow next"><svg width="10" height="14" viewBox="0 0 10 14"><path d="M2 1l6 6-6 6" fill="none" stroke="#fff" stroke-width="2"/></svg></div>
  </div>
</section>

<section class="section search">
  <span class="field-label" style="left:99px">Min of Bedrooms</span>
  <span class="field-label" style="left:349px">Min of Bathrooms</span>
  <span class="field-label" style="left:607px">Min Area</span>
  <span class="field-label" style="left:864px">Max Area (Sqft)</span>
  <div class="field-select" style="left:99px">Any</div>
  <div class="field-select" style="left:349px">Any</div>
  <div class="field-select" style="left:607px">Any</div>
  <div class="field-select" style="left:864px">Any</div>
  <span class="range-label">Pricing Range</span>
  <div class="range-track">
    <div class="range-fill"></div>
    <div class="range-knob" style="left:85px"></div>
    <div class="range-knob" style="left:385px"></div>
  </div>
  <span class="range-value">$10000 - $30000</span>
  <div class="btn-search">SEARCH</div>
</section>

<section class="section about">
  <h2 class="section-title">ABOUT US</h2>
  <p class="lead">We help families and investors find homes that fit the way they live. Our local team knows every street, school and market shift, and we guide each client from first viewing to final key handover with care and clear advice.</p>
  <h3 class="sub-title" style="top:222px">Our Story</h3>
  <p class="about-text" style="top:258px">Dean Harlow started with one small office and a promise to treat every sale as if it were our own home. Years later that promise still shapes how we list, market and negotiate for every client we serve across the region.</p>
  <h3 class="sub-title" style="top:397px">Our Mission</h3>
  <p class="about-text" style="top:432px">Our mission is to make buying, selling and renting simple, honest and rewarding. We combine sharp market insight with friendly service so every client moves forward with confidence and a result they are proud of.</p>
  <div class="about-video" role="img" aria-label="Modern two storey house with a pool at dusk">
    <div class="play"><svg width="20" height="22" viewBox="0 0 20 22"><path d="M3 2l15 9-15 9z" fill="#fff"/></svg></div>
    <div class="video-caption">Real Estate<small>BOOK TODAY VIEWING</small></div>
  </div>
</section>

<section class="section featured">
  <h2 class="section-title">FEATURED PROEPRTY</h2>
  <p class="lead">Browse a hand picked selection of homes, land and commercial spaces currently on our books, each chosen for location, quality and value.</p>
  <div class="tabs">
    <span class="tab active">All</span><span class="tab">Commercial</span><span class="tab">Furnished Home</span><span class="tab">Land &amp; Plot</span><span class="tab">Residential</span>
  </div>

  <div class="prop-card" style="left:105px;top:280px"><div class="prop-photo" role="img" aria-label="White villa with pool" style="background:linear-gradient(180deg,#8fc2ea,#e6eaec 55%,#3aa0d8)"></div><div class="tag-sale">For<br>Sale</div><div class="prop-name">ELM TOWER, SURREY, NJ</div><div class="prop-loc">United States / South Dakota</div><div class="prop-price">$10000</div></div>
  <div class="prop-card" style="left:435px;top:280px"><div class="prop-photo" role="img" aria-label="Modern house with lawn" style="background:linear-gradient(180deg,#d4dde4,#9aa3a8 55%,#7c9a5e)"></div><div class="tag-sale">For<br>Rent</div><div class="prop-name">ELM TOWER, SURREY, NJ</div><div class="prop-loc">United States / South Dakota</div><div class="prop-price">$40000</div></div>
  <div class="prop-card" style="left:765px;top:280px"><div class="prop-photo" role="img" aria-label="Contemporary villa with pool" style="background:linear-gradient(180deg,#a8cde8,#e8ebec 55%,#55a8d4)"></div><div class="tag-sale">For<br>Sale</div><div class="prop-name">ELM TOWER, SURREY, NJ</div><div class="prop-loc">United States / South Dakota</div><div class="prop-price">$10000</div></div>

  <div class="prop-card" style="left:105px;top:561px"><div class="prop-photo" role="img" aria-label="White cube house on a lawn" style="background:linear-gradient(180deg,#9ac4e6,#eeeeee 55%,#6e9a56)"></div><div class="tag-sale">For<br>Sale</div><div class="prop-name">ELM TOWER, SURREY, NJ</div><div class="prop-loc">United States / South Dakota</div><div class="prop-price">$80000</div></div>
  <div class="prop-card" style="left:435px;top:561px"><div class="prop-photo" role="img" aria-label="Grey modern house at dusk" style="background:linear-gradient(180deg,#8a9aae,#6a6c70 55%,#4e5a4a)"></div><div class="tag-sale">For<br>Rent</div><div class="prop-name">ELM TOWER, SURREY, NJ</div><div class="prop-loc">United States / South Dakota</div><div class="prop-price">$40000</div></div>
  <div class="prop-card" style="left:765px;top:561px"><div class="prop-photo" role="img" aria-label="Lit modern house at night" style="background:linear-gradient(180deg,#3a4a66,#b88a56 55%,#3c3a36)"></div><div class="tag-sale">For<br>Sale</div><div class="prop-name">ELM TOWER, SURREY, NJ</div><div class="prop-loc">United States / South Dakota</div><div class="prop-price">$10000</div></div>

  <div class="prop-card" style="left:105px;top:834px"><div class="prop-photo" role="img" aria-label="Pool house with palm trees" style="background:linear-gradient(180deg,#86c0ea,#e4e4e0 55%,#2ea0da)"></div><div class="tag-sale">For<br>Sale</div><div class="prop-name">ELM TOWER, SURREY, NJ</div><div class="prop-loc">United States / South Dakota</div><div class="prop-price">$10000</div></div>
  <div class="prop-card" style="left:435px;top:834px"><div class="prop-photo" role="img" aria-label="Flat roof villa in evening light" style="background:linear-gradient(180deg,#6f8fb8,#d9c8a8 55%,#7a7064)"></div><div class="tag-sale">For<br>Rent</div><div class="prop-name">ELM TOWER, SURREY, NJ</div><div class="prop-loc">United States / South Dakota</div><div class="prop-price">$40000</div></div>
  <div class="prop-card" style="left:765px;top:834px"><div class="prop-photo" role="img" aria-label="Timber and glass house at sunset" style="background:linear-gradient(180deg,#4f6a8a,#c48a52 55%,#4a3a2e)"></div><div class="tag-sale">For<br>Sale</div><div class="prop-name">ELM TOWER, SURREY, NJ</div><div class="prop-loc">United States / South Dakota</div><div class="prop-price">$40000</div></div>

  <div class="btn-more">LOAD MORE</div>
</section>

<section class="section highlights">
  <h2 class="hl-title">Property Highlights</h2>
  <p class="hl-text">Extensive upgrades and thorough maintenance have kept this home in prime condition. Hardwood floors and new carpets create a very comfortable living space.</p>
  <div class="hl-feature" style="left:99px;top:185px">
    <svg width="22" height="22" viewBox="0 0 22 22"><path d="M2 11l9-8 9 8M5 9v10h12V9" fill="none" stroke="#2ecc71" stroke-width="2"/></svg>
    <h4>Quiet Neighbourhood</h4><p>Enjoy tranquil and relaxed atmosphere of the place</p>
  </div>
  <div class="hl-feature" style="left:345px;top:185px">
    <svg width="22" height="22" viewBox="0 0 22 22"><circle cx="8" cy="8" r="4" fill="none" stroke="#2ecc71" stroke-width="2"/><circle cx="16" cy="9" r="3" fill="none" stroke="#2ecc71" stroke-width="2"/><path d="M1 20c0-4 3-7 7-7s7 3 7 7" fill="none" stroke="#2ecc71" stroke-width="2"/></svg>
    <h4>Great local community</h4><p>You will be delighted by the fantastic local community</p>
  </div>
  <div class="hl-feature" style="left:99px;top:265px">
    <svg width="22" height="22" viewBox="0 0 22 22"><path d="M1 11s4-7 10-7 10 7 10 7-4 7-10 7S1 11 1 11z" fill="none" stroke="#2ecc71" stroke-width="2"/><circle cx="11" cy="11" r="3" fill="#2ecc71"/></svg>
    <h4>Fabulous views</h4><p>Get yourself surrounded by the stunning view opening</p>
  </div>
  <div class="hl-feature" style="left:345px;top:265px">
    <svg width="22" height="22" viewBox="0 0 22 22"><rect x="2" y="6" width="18" height="12" fill="none" stroke="#2ecc71" stroke-width="2"/><path d="M2 12h18M11 6v12" stroke="#2ecc71" stroke-width="2"/></svg>
    <h4>Large play center in yard</h4><p>Your kids will be happy having all these things around</p>
  </div>
  <div class="btn-green">LOAD MORE</div>
  <div class="hl-photo" role="img" aria-label="White modern house with a long pool and terrace"></div>
  <div class="hl-arrow" style="left:610px"><svg width="8" height="12" viewBox="0 0 8 12"><path d="M7 1L2 6l5 5" fill="none" stroke="#fff" stroke-width="2"/></svg></div>
  <div class="hl-arrow" style="left:1058px"><svg width="8" height="12" viewBox="0 0 8 12"><path d="M1 1l5 5-5 5" fill="none" stroke="#fff" stroke-width="2"/></svg></div>
</section>

<section class="section listings">
  <h2 class="section-title">LATEST LISTINGS</h2>
  <div class="side-arrow" style="left:26px"><svg width="10" height="14" viewBox="0 0 10 14"><path d="M8 1L2 7l6 6" fill="none" stroke="#fff" stroke-width="2"/></svg></div>
  <div class="side-arrow" style="left:1112px"><svg width="10" height="14" viewBox="0 0 10 14"><path d="M2 1l6 6-6 6" fill="none" stroke="#fff" stroke-width="2"/></svg></div>

  <article class="list-card" style="left:99px">
    <div class="list-photo" role="img" aria-label="Sunlit living room with large windows" style="background:linear-gradient(135deg,#e8e2d6,#c9b89c 50%,#8a7a66)"></div>
    <span class="tag-excl">Exclusive</span><span class="tag-rent">$3,000/mo</span>
    <div class="list-name">The Alder Residences Review</div>
    <div class="list-addr">26 Westbrook Lane, Dunmore, NSW 2041</div>
    <div class="list-spec">Bedroom: 4 &nbsp;Bathroom: 2 &nbsp;Land Size: 3000 square<br>Building Size: 2400 square<br>House</div>
    <div class="list-foot"><span>NORA BELL</span><span>7 months ago</span></div>
  </article>
  <article class="list-card" style="left:435px">
    <div class="list-photo" role="img" aria-label="Dark modern lounge with orange accents" style="background:linear-gradient(135deg,#4a4a4c,#2c2c2e 50%,#b8562e)"></div>
    <span class="tag-excl">Exclusive</span><span class="tag-rent">$3,000/mo</span>
    <div class="list-name">Bayview Residences</div>
    <div class="list-addr">52 Crescent Road, Ashfield Park, NSW 2044</div>
    <div class="list-spec">Bedroom: 4 &nbsp;Bathroom: 2 &nbsp;Land Size: 3000 square<br>Building Size: 2400 square<br>House</div>
    <div class="list-foot"><span>OWEN PRICE</span><span>7 months ago</span></div>
  </article>
  <article class="list-card" style="left:771px">
    <div class="list-photo" role="img" aria-label="Bright open kitchen and dining area" style="background:linear-gradient(135deg,#f0ece4,#d8c8ae 50%,#6f8a5a)"></div>
    <span class="tag-excl">Exclusive</span><span class="tag-rent">$3,000/mo</span>
    <div class="list-name">Wrenfield Residence</div>
    <div class="list-addr">9 Orchard Street, Hillcrest, NSW 2043</div>
    <div class="list-spec">Bedroom: 4 &nbsp;Bathroom: 2 &nbsp;Land Size: 3000 square<br>Building Size: 2400 square<br>Flat</div>
    <div class="list-foot"><span>TESSA VALE</span><span>7 months ago</span></div>
  </article>
</section>

<section class="section testimonial">
  <h2 class="section-title">WHAT OUR CLIENT SAYS?</h2>
  <div class="client-photo" role="img" aria-label="Portrait of a smiling client"></div>
  <p class="quote">The team made selling our family home easy from start to finish, always honest, quick to reply and focused on the best price for us.</p>
  <div class="client-name">Liam Carter, Happy Owner, Parkside, Sydney</div>
  <div class="dots"><span class="on"></span><span></span><span></span></div>
</section>

<section class="section newsletter">
  <h2 class="section-title">SUBSCRIBE NEWSLETTER</h2>
  <div class="news-input">Please type your email id</div>
  <div class="news-btn">SUBSCRIBE</div>
</section>

<footer class="section site-footer">
  <div class="foot-col" style="left:73px">
    <h5>Contacts</h5>
    <p>We are the local real estate team dedicated to helping every client find the right home.</p>
    <div class="contact-line"><svg width="12" height="14" viewBox="0 0 12 14"><path d="M6 13S1 8 1 5a5 5 0 0110 0c0 3-5 8-5 8z" fill="#2196f3"/></svg><p>48 Corran Street, VIC</p></div>
    <div class="contact-line"><svg width="12" height="12" viewBox="0 0 12 12"><path d="M2 1l3 1-1 3 3 3 3-1 1 3-2 1C5 11 1 7 1 3z" fill="#2196f3"/></svg><p>+61 400 555 019</p></div>
    <div class="contact-line"><svg width="12" height="10" viewBox="0 0 12 10"><rect x="1" y="1" width="10" height="8" fill="none" stroke="#2196f3" stroke-width="1.5"/><path d="M1 1l5 4 5-4" fill="none" stroke="#2196f3" stroke-width="1.5"/></svg><p>hello@deanharlow-example.com</p></div>
  </div>
  <div class="foot-col" style="left:336px">
    <h5>From the Blog</h5>
    <div class="post"><div class="post-thumb" role="img" aria-label="Small furnished room"></div><div><b>Making the Most of Your Small Space with Furniture</b><small>MARCH 6, 2018</small></div></div>
    <div class="post"><div class="post-thumb" role="img" aria-label="Apartment interior"></div><div><b>4 Ways to Decorate Your First Apartment on a Budget</b><small>MARCH 6, 2018</small></div></div>
    <div class="post"><div class="post-thumb" role="img" aria-label="Room with natural light"></div><div><b>How to Infuse Your Space with Natural Light</b><small>MARCH 6, 2018</small></div></div>
  </div>
  <div class="foot-col quick" style="left:603px;width:200px">
    <h5>Quick Links</h5>
    <ul><li>HOME</li><li>BLOG</li><li>ABOUT US</li><li>LISTING</li><li>GALLERY</li><li>CONTACT</li></ul>
  </div>
  <div class="foot-col" style="left:864px;width:250px">
    <h5>Latest Tweets</h5>
    <p class="tweet"><b>@HarlowHomes</b> New listing this week: a bright family home with garden and pool.</p>
    <p class="tweet"><b>@HarlowHomes</b> Thinking of selling? Book a free appraisal with our local team today.</p>
  </div>
</footer>

<div class="section copyright">
  <div class="copy-text">© All Rights Reserved Dean Harlow Property</div>
  <div class="social"><span></span><span></span><span></span><span></span><span></span><span></span></div>
</div>

</body>
</html>
```